Business Card Design Project

I have attached the logo and the colour pallete for the branding for the company.

Creative designs for business cards are needed.

The Company is modern corporate.

Industry/Entity Type

Business

```html
<!DOCTYPE html>
<html lang="en">
<head>
<meta charset="utf-8">
<title>Routewise Business Card</title>
<link rel="stylesheet" href="https://fonts.googleapis.com/css2?family=Didact+Gothic&display=swap">
<style>
  :root {
    --backdrop: #3b2419;
    --card-black: #050505;
    --card-glow: #1e1e1e;
    --band-deep: #cf8d2c;
    --band-light: #efad3b;
    --ink-light: #ffffff;
    --ink-cream: #fff6e6;
  }
  * { margin: 0; padding: 0; box-sizing: border-box; }
  html, body {
    width: 1200px;
    height: 1181px;
    overflow: hidden;
    background: var(--backdrop);
  }
  .canvas {
    position: relative;
    width: 1200px;
    height: 1181px;
    font-family: "Didact Gothic", sans-serif;
  }
  .card {
    position: absolute;
    left: 230px;
    width: 741px;
    height: 426px;
    border-radius: 28px;
    overflow: hidden;
    background: radial-gradient(ellipse 55% 60% at 50% 50%, var(--card-glow) 0%, var(--card-black) 100%);
    box-shadow: 0 6px 14px rgba(0, 0, 0, 0.55);
  }
  .card--front { top: 128px; }
  .card--back { top: 617px; }
  .band {
    position: absolute;
    left: 0;
    top: 150px;
    width: 100%;
    height: 125px;
    background: linear-gradient(90deg, var(--band-deep) 0%, var(--band-light) 55%, var(--band-deep) 100%);
    box-shadow: 0 4px 10px rgba(0, 0, 0, 0.6), 0 -4px 10px rgba(0, 0, 0, 0.6);
  }
  .brand-name {
    position: absolute;
    left: 0;
    right: 0;
    top: 22px;
    text-align: center;
    font-size: 68px;
    line-height: 80px;
    color: var(--ink-light);
    letter-spacing: -1px;
  }
  .identity {
    position: absolute;
    right: 405px;
    top: 33px;
    text-align: right;
    color: var(--ink-cream);
  }
  .identity__name { font-size: 28px; line-height: 30px; }
  .identity__role { font-size: 21px; line-height: 22px; }
  .divider {
    position: absolute;
    left: 366px;
    top: 10px;
  }
  .contact {
    position: absolute;
    left: 400px;
    top: 30px;
    list-style: none;
    color: var(--ink-cream);
    font-size: 16px;
    line-height: 21px;
  }
</style>
</head>
<body>
<main class="canvas">
  <section class="card card--front" aria-label="Card front">
    <div class="band">
      <p class="brand-name">Routewise</p>
    </div>
  </section>

  <section class="card card--back" aria-label="Card back">
    <div class="band">
      <div class="identity">
        <p class="identity__name">Your Full Name</p>
        <p class="identity__role">Your position</p>
      </div>
      <svg class="divider" width="8" height="104" viewBox="0 0 8 104" aria-hidden="true">
        <ellipse cx="4" cy="52" rx="1.8" ry="51" fill="#ffffff"/>
      </svg>
      <ul class="contact">
        <li>Tel. (123) 456-7890</li>
        <li>email: yourname@email.com</li>
        <li>Find us on Friendloop!</li>
      </ul>
    </div>
  </section>
</main>
</body>
</html>
```